Welcome Card Banner Desing for email suscriptors

to get involved on this task please check my site tulavendo.app
I wish for this task a welcome postal card to get subscribers for the newsletter and get a Coupon Code for discounts,
Keep in mind Velisso is a platform where customers (girls) can get any fashion high-end accessories ready to wear, to see the categories please visit our shop.

Target Market(s)

World wide people between 18-60 years old

Industry/Entity Type

Fashion

Coding

Coded - Design and coding required

Number of Pages Required

1 page

Font styles to use
Sans Serif

Colors
a64599
ffffff
ffc214
faa54b

Requirements
Must have
• Simplicity
• to get involved on this task please check my site tulavendo.app
• I wish for this task a welcome postal card to get subscribers for the newsletter and get a Coupon Code for discounts,
• Keep in mind Velisso is a platform where customers (girls) can get any fashion high-end accessories ready to wear, to see the categories please visit our shop.
Nice to have
• Field for customer fill an email or just skip the banner
Should not have
• Bad grammar

```html
<!DOCTYPE html>
<html lang="en">
<head>
<meta charset="UTF-8">
<title>Velisso – Welcome Card</title>
<link rel="stylesheet" href="https://fonts.googleapis.com/css2?family=Arimo:wght@400;700&display=swap">
<style>
  :root {
    --stage: #3d3d3d;
    --card-frame: #f0efed;
    --band: #f0efed;
    --ink: #2b2b2b;
    --white: #ffffff;
    --discount: #b5651f;
    --paper-light: #d4ae78;
    --paper-mid: #c59a62;
    --paper-dark: #a9773f;
    --photo-top: #8c8a86;
    --photo-mid: #b4561f;
    --photo-low: #4a3a30;
    --photo-accent: #b3242a;
  }
  * { box-sizing: border-box; margin: 0; padding: 0; }
  html, body {
    width: 1200px;
    height: 580px;
    overflow: hidden;
    background: var(--stage);
    font-family: "Arimo", Helvetica, Arial, sans-serif;
  }
  .welcome-card {
    position: absolute;
    left: 187px;
    top: 10px;
    width: 826px;
    height: 560px;
    background: var(--card-frame);
    padding: 21px 19px 18px 25px;
    display: flex;
  }
  .welcome-panel {
    position: relative;
    width: 434px;
    height: 521px;
    overflow: hidden;
  }
  .welcome-photo {
    position: absolute;
    inset: 0;
    background:
      radial-gradient(ellipse 40% 35% at 18% 78%, rgba(179,36,42,0.55), transparent 70%),
      radial-gradient(ellipse 45% 55% at 70% 60%, rgba(196,92,32,0.9), transparent 75%),
      linear-gradient(180deg, var(--photo-top) 0%, #9b8f86 35%, var(--photo-mid) 62%, var(--photo-low) 100%);
  }
  .welcome-title {
    position: absolute;
    top: 64px;
    left: 0;
    width: 100%;
    text-align: center;
    color: var(--white);
    font-weight: 700;
    font-size: 55px;
    line-height: 66px;
    letter-spacing: 0.5px;
    text-shadow: 2px 3px 4px rgba(0,0,0,0.45);
  }
  .subscribe-band {
    position: absolute;
    top: 352px;
    left: 0;
    width: 426px;
    height: 58px;
    background: var(--band);
    color: var(--ink);
    font-weight: 700;
    font-size: 27px;
    display: flex;
    align-items: center;
    justify-content: center;
  }
  .discount-panel {
    position: relative;
    width: 347px;
    height: 521px;
    text-align: center;
  }
  .paper-texture {
    position: absolute;
    inset: 0;
    background:
      radial-gradient(ellipse 70% 60% at 50% 45%, var(--paper-light), transparent 80%),
      linear-gradient(160deg, var(--paper-mid), var(--paper-dark));
  }
  .notch {
    position: absolute;
    left: 165px;
    width: 16px;
    height: 16px;
    border-radius: 50%;
    background: var(--white);
  }
  .notch--top { top: -8px; }
  .notch--bottom { bottom: -8px; }
  .discount-title {
    position: absolute;
    top: 88px;
    width: 100%;
    font-size: 57px;
    color: var(--discount);
    opacity: 0.85;
  }
  .discount-amount {
    position: absolute;
    top: 152px;
    width: 100%;
    font-size: 38px;
    color: var(--ink);
  }
  .coupon-button {
    position: absolute;
    top: 259px;
    left: 54px;
    width: 239px;
    height: 36px;
    border: 1px dashed var(--ink);
    color: var(--white);
    font-weight: 700;
    font-size: 18px;
    display: flex;
    align-items: center;
    justify-content: center;
    text-shadow: 1px 1px 2px rgba(0,0,0,0.5);
  }
  .brand-name {
    position: absolute;
    top: 457px;
    width: 100%;
    font-weight: 700;
    font-size: 18px;
    color: var(--ink);
  }
  .copyright {
    position: absolute;
    top: 484px;
    width: 100%;
    font-size: 8px;
    color: var(--ink);
  }
</style>
</head>
<body>
  <section class="welcome-card">
    <div class="welcome-panel">
      <div class="welcome-photo" role="img" aria-label="Photo of a woman in red glitter heels holding an orange leather handbag"></div>
      <h1 class="welcome-title">"Welcome<br>to the finest<br>shop"</h1>
      <div class="subscribe-band">Subscribe</div>
    </div>
    <div class="discount-panel">
      <div class="paper-texture" role="img" aria-label="Aged brown paper texture"></div>
      <span class="notch notch--top"></span>
      <span class="notch notch--bottom"></span>
      <h2 class="discount-title">Discount</h2>
      <p class="discount-amount">Upto 30%</p>
      <div class="coupon-button">get coupon code</div>
      <p class="brand-name">Velisso</p>
      <p class="copyright">©Copyright 2019, Velisso</p>
    </div>
  </section>
</body>
</html>
```